" Abrimos o escritório há poucos meses. Somos duas mulheres, a Sofia recém formada e a Berta formada há pouco mais de quatro anos. Estamos iniciando nossa carreira como advogadas esse ano, por enquanto, trabalhamos nós duas atuando nas mais diversas áreas do direito, sobretudo, cível, previdenciário e criminal. "

```html
<!DOCTYPE html>
<html lang="pt-BR">
<head>
<meta charset="UTF-8">
<title>Ferraz &amp; Moura Advocacia — Pasta</title>
<link rel="stylesheet" href="https://fonts.googleapis.com/css2?family=Cinzel:wght@400&family=Arimo:wght@400&display=swap">
<style>
  :root {
    --backdrop: #d9d6d4;
    --burgundy: #4d0a1d;
    --burgundy-flap: #5a1026;
    --burgundy-fold: #41081a;
    --gold-light: #f0d2a6;
    --gold: #c79a66;
    --gold-dark: #8a5f36;
    --ink-light: #f3e9ea;
  }
  * { margin: 0; padding: 0; box-sizing: border-box; }
  html, body { width: 1200px; height: 1200px; overflow: hidden; }
  body { background: var(--backdrop); position: relative; font-family: "Arimo", Arial, sans-serif; }

  .folder-art { position: absolute; inset: 0; }

  .brand {
    position: absolute;
    left: 676px; top: 470px; width: 400px;
    text-align: center;
    color: var(--ink-light);
  }
  .brand-name {
    font-family: "Cinzel", serif;
    font-size: 36px;
    letter-spacing: 1px;
    line-height: 1;
    color: var(--gold-light);
  }
  .brand-rule {
    height: 2px; width: 330px; margin: 14px auto 10px;
    background: linear-gradient(90deg, transparent, var(--gold) 20%, var(--gold-light) 50%, var(--gold) 80%, transparent);
  }
  .brand-area {
    font-family: "Cinzel", serif;
    font-size: 17px;
    letter-spacing: 9px;
    color: var(--ink-light);
  }

  .contact {
    position: absolute;
    left: 110px; top: 796px; width: 460px;
    text-align: center;
    color: var(--ink-light);
    font-size: 13px;
    line-height: 16px;
  }
  .contact-phones span + span { margin-left: 22px; }
  .contact-address { white-space: nowrap; }

  .website {
    position: absolute;
    left: 800px; top: 826px;
    color: var(--ink-light);
    font-size: 13px;
  }
</style>
</head>
<body>
  <svg class="folder-art" width="1200" height="1200" viewBox="0 0 1200 1200" aria-hidden="true">
    <defs>
      <linearGradient id="gold-band" x1="0" x2="1" y1="0" y2="0">
        <stop offset="0" stop-color="var(--gold-dark)"/>
        <stop offset="0.35" stop-color="var(--gold-light)"/>
        <stop offset="0.65" stop-color="var(--gold)"/>
        <stop offset="1" stop-color="var(--gold-dark)"/>
      </linearGradient>
    </defs>
    <!-- pocket flap -->
    <path class="pocket-flap" d="M84 852 H560 C610 852 640 880 620 930 C590 990 520 1010 470 1056 H84 Z" fill="var(--burgundy-flap)"/>
    <!-- folder body -->
    <rect class="folder-body" x="84" y="132" width="984" height="720" fill="var(--burgundy)"/>
    <!-- spine fold -->
    <rect class="spine-fold" x="598" y="132" width="4" height="720" fill="var(--burgundy-fold)"/>
    <!-- gold band -->
    <rect class="gold-band" x="84" y="848" width="984" height="5" fill="url(#gold-band)"/>
  </svg>

  <div class="brand">
    <div class="brand-name">Ferraz &amp; Moura</div>
    <div class="brand-rule"></div>
    <div class="brand-area">ADVOCACIA</div>
  </div>

  <div class="contact">
    <div class="contact-email">contato@ferrazmoura.adv.br</div>
    <div class="contact-phones"><span>(11) 3000-4000</span><span>(11) 90000-5000</span></div>
    <div class="contact-address">Rua das Acácias nº 120 - Vila Serena - São Paulo - SP - 01234-050</div>
  </div>

  <div class="website">www.ferrazmoura.adv.br</div>
</body>
</html>
```